Fundraising Flyer for a School Library

We are a small but fast-growing school in need of funding support for a new Library, Admin and 2 more primary classrooms.
We are hoping that someone can come up with a design for a flyer (A4 - 3 fold) or brochure (2 to an A4) that will encourage people in our community to consider 'partnering' with us to help fund this massive project.
The 'Word' doc attached has some initial wording ideas, however someone with a gift for this type of advertising may well come up with better wording. We're happy for you to use a bit of creativity here.

Target Market(s)

Local businesses, parents and extended families

Industry/Entity Type

School

Requirements
Must have
• Picture of the proposed library.
• Pictures of students from our school.
• You can find information and photos on our school website. http://www.pkrts.example.edu.au/
Should not have
• Anything inappropriate for a Christian School.
• Pictures of random people that aren't from our school - ie, aren't in our school uniform.

```html
<!DOCTYPE html>
<html lang="en">
<head>
<meta charset="utf-8">
<title>Investing in Tomorrow – Building Fund Brochure</title>
<link rel="stylesheet" href="https://fonts.googleapis.com/css2?family=Raleway:wght@300;400;800&family=Roboto+Condensed:wght@300;400;700&display=swap">
<style>
:root{
  --bg:#e6e6e6;
  --paper:#ffffff;
  --sky:#3fa9e0;
  --red:#e1262d;
  --teal:rgba(40,170,190,.72);
  --teal-solid:#2aa6bb;
  --navy:#1f2c4a;
  --slate:#8c8782;
  --slate-dark:#6f6a65;
  --ink:#ffffff;
}
*{box-sizing:border-box;margin:0;padding:0}
html,body{width:1200px;height:1000px;overflow:hidden;background:var(--bg)}
body{position:relative;font-family:"Roboto Condensed",sans-serif}
.spread{position:absolute;left:260px;width:680px;height:481px;display:flex;box-shadow:0 6px 18px rgba(0,0,0,.18)}
.spread--outer{top:12px}
.spread--inner{top:507px;background:var(--slate)}
.page{position:relative;width:340px;height:481px;overflow:hidden}

/* back page */
.back-photo{position:absolute;inset:0;background:linear-gradient(135deg,#c9a34a 0%,#e6c36a 35%,#d9b98a 60%,#b8863e 100%)}
.intro-box{position:absolute;left:26px;top:28px;width:228px;height:320px;background:var(--teal);padding:14px 14px;color:var(--ink)}
.mini-brand{display:flex;align-items:center;gap:6px;font-weight:700;font-size:11px;margin-bottom:10px}
.mini-brand .dot{width:16px;height:16px;border-radius:50%;background:var(--ink)}
.intro-box p{font-size:11.5px;line-height:1.45;text-transform:uppercase;font-weight:300}

/* front cover */
.cover{background:var(--paper)}
.cover-photo{position:absolute;left:14px;top:14px;width:312px;height:300px;background:linear-gradient(160deg,#e8eef3 0%,#8aa6bd 30%,#2c4c72 65%,#18284a 100%)}
.cover-banner{position:absolute;left:14px;top:92px;width:150px;height:120px;background:var(--teal);color:var(--ink);padding:38px 10px 0 12px;text-align:right}
.cover-banner .small{font-family:"Raleway",sans-serif;font-weight:300;font-size:13px;letter-spacing:.5px}
.cover-banner .big{font-family:"Raleway",sans-serif;font-weight:800;font-size:22px;letter-spacing:.5px}
.slogan{position:absolute;left:16px;top:326px;font-family:"Raleway",sans-serif;line-height:1;font-size:27px;text-transform:uppercase}
.slogan .bold{font-weight:800;display:block}
.slogan .light{font-weight:300;display:block;margin-bottom:4px}
.slogan .blue{color:var(--sky)}
.slogan .red{color:var(--red)}
.brand{position:absolute;right:14px;top:340px;width:96px;display:flex;flex-direction:column;align-items:center;gap:6px;text-align:center}
.brand .mark{width:52px;height:52px;border-radius:50%;background:var(--navy)}
.brand .name{font-family:"Raleway",sans-serif;font-weight:800;font-size:11px;color:var(--navy);line-height:1.15;text-transform:uppercase}

/* inner left */
.partners{position:absolute;left:14px;top:14px;display:flex;align-items:center;gap:8px}
.partners .badge{width:56px;height:56px;border-radius:50%;background:var(--red);color:var(--ink);display:flex;align-items:center;justify-content:center;font-weight:700;font-size:18px}
.partners h2{font-family:"Raleway",sans-serif;font-weight:800;color:var(--red);font-size:30px;line-height:.95;text-transform:uppercase}
.rule-title{position:absolute;display:flex;align-items:center;gap:8px;color:var(--ink);font-size:12px;letter-spacing:1px;text-transform:uppercase}
.rule-title::before,.rule-title::after{content:"";height:1px;width:40px;background:var(--ink);opacity:.8}
.raise{left:90px;top:84px}
.amount{position:absolute;left:120px;top:104px;color:var(--red);font-weight:700;font-size:24px;line-height:1}
.fund{position:absolute;left:16px;top:158px;width:190px;color:var(--ink);font-size:12px;line-height:1.15;text-transform:uppercase;font-weight:700}
.cost{position:absolute;left:16px;top:190px;width:200px;color:var(--ink);font-size:9px;text-transform:uppercase}
.photo{position:absolute;border:2px solid rgba(255,255,255,.7)}
.library-photo{left:70px;top:212px;width:150px;height:96px;background:linear-gradient(180deg,#a9c7e0 0%,#c7d6e4 45%,#d9cdb8 70%,#7d8f5a 100%)}
.arrow{position:absolute;left:220px;top:140px}
.audience{position:absolute;color:var(--ink);text-transform:uppercase;line-height:1.05}
.a1{left:24px;top:330px;font-size:13px}
.a2{left:118px;top:324px;font-size:13px;letter-spacing:1px}
.a3{left:118px;top:342px;font-size:20px;font-weight:700}
.a4{left:236px;top:340px;font-size:13px}
.a5{left:30px;top:384px;font-size:12px}
.a6{left:30px;top:402px;font-size:13px}
.a7{left:170px;top:420px;font-size:13px}

/* inner right */
.donate{left:50px;top:18px}
.grid{position:absolute;left:14px;top:40px;width:312px;height:320px}
.p1{left:0;top:0;width:70px;height:62px;background:linear-gradient(160deg,#8ba7c6,#6b7f52)}
.p2{left:74px;top:0;width:92px;height:62px;background:linear-gradient(160deg,#7e8aa0,#3e4d6a)}
.p3{left:0;top:70px;width:104px;height:88px;background:linear-gradient(160deg,#4f6a8a,#2b3a55)}
.p4{left:0;top:166px;width:60px;height:52px;background:linear-gradient(160deg,#6a6f84,#2e3448)}
.p5{left:64px;top:166px;width:60px;height:52px;background:linear-gradient(160deg,#8aa07a,#4f6b3a)}
.p6{left:130px;top:190px;width:80px;height:60px;background:linear-gradient(160deg,#7fa86a,#3e6b33)}
.p7{left:216px;top:190px;width:92px;height:60px;background:linear-gradient(160deg,#9aa7b2,#5f6b74)}
.p8{left:60px;top:226px;width:66px;height:58px;background:linear-gradient(160deg,#3a2f2a,#151212)}
.p9{left:130px;top:258px;width:90px;height:58px;background:linear-gradient(160deg,#86a0b8,#4a5f72)}
.p10{left:224px;top:258px;width:84px;height:58px;background:linear-gradient(160deg,#b09a7a,#5d5a50)}
.chart-box{position:absolute;left:170px;top:0;width:142px;height:112px;background:var(--red)}
.ways{position:absolute;left:100px;top:120px;width:214px;background:var(--red);color:var(--ink);padding:6px 8px;font-size:10px;line-height:1.3;text-transform:uppercase;font-weight:700}
.ways span{display:block}
.ways .site{font-weight:400;text-transform:none}
.notice{position:absolute;left:18px;top:380px;width:304px;color:var(--ink);font-size:10px;line-height:1.35;text-transform:uppercase}
</style>
</head>
<body>

<section class="spread spread--outer">
  <article class="page back">
    <div class="back-photo" role="img" aria-label="Photo of students doing a science experiment with coloured test tubes"></div>
    <div class="intro-box">
      <div class="mini-brand"><span class="dot"></span>Parkridge Valley</div>
      <p>Parkridge Valley Christian School provides quality Christ centred education for families across our valley. Our students grow in faith, character and learning within a caring community. We are committed to helping each child reach their full potential and become a servant leader. Please contact the school office to arrange a visit and see our school in action.</p>
    </div>
  </article>

  <article class="page cover">
    <div class="cover-photo" role="img" aria-label="Photo of a curved wall of library bookshelves"></div>
    <div class="cover-banner">
      <div class="small">INVESTING IN</div>
      <div class="big">TOMORROW</div>
    </div>
    <h1 class="slogan">
      <span class="bold blue">Children</span>
      <span class="light blue">of today</span>
      <span class="bold red">Leaders</span>
      <span class="light red">of tomorrow</span>
    </h1>
    <div class="brand">
      <span class="mark"></span>
      <span class="name">Parkridge Valley C.S.</span>
    </div>
  </article>
</section>

<section class="spread spread--inner">
  <article class="page inner-left">
    <div class="partners">
      <div class="badge">100</div>
      <h2>Partners<br>Sought</h2>
    </div>
    <div class="rule-title raise">To raise</div>
    <div class="amount">$50,000<br>OR MORE</div>
    <p class="fund">By tax deductible donations to the PVCS building fund</p>
    <p class="cost">The total cost of the construction is $1.2 million</p>
    <div class="photo library-photo" role="img" aria-label="Render of the proposed new library building"></div>
    <svg class="arrow" width="110" height="110" viewBox="0 0 110 110" aria-hidden="true">
      <path d="M10 100 L10 60 L55 60 L55 30 L100 70 L55 110 Z" fill="var(--red)" opacity=".85" transform="translate(0,-10)"/>
    </svg>
    <div class="audience a1">School<br>Families</div>
    <div class="audience a2">Please</div>
    <div class="audience a3">Church<br>Members</div>
    <div class="audience a4">Christian<br>Community</div>
    <div class="audience a5">Grandparents</div>
    <div class="audience a6">Parkridge Valley businesses</div>
    <div class="audience a7">and others...</div>
  </article>

  <article class="page inner-right">
    <div class="rule-title donate">Donate to the community</div>
    <div class="grid">
      <div class="photo p1" role="img" aria-label="Photo of a ribbon cutting at the school"></div>
      <div class="photo p2" role="img" aria-label="Photo of school staff at an opening"></div>
      <div class="photo p3" role="img" aria-label="Photo of students in class"></div>
      <div class="photo p4" role="img" aria-label="Photo of students in uniform"></div>
      <div class="photo p5" role="img" aria-label="Photo of students outdoors"></div>
      <div class="photo p6" role="img" aria-label="Photo of students on the school oval"></div>
      <div class="photo p7" role="img" aria-label="Photo of a school group"></div>
      <div class="photo p8" role="img" aria-label="Photo of a school performance on stage"></div>
      <div class="photo p9" role="img" aria-label="Photo of students at their desks"></div>
      <div class="photo p10" role="img" aria-label="Photo of students at an event"></div>
      <div class="chart-box">
        <svg width="142" height="112" viewBox="0 0 142 112" role="img" aria-label="Donation levels from $100 to $2000">
          <g fill="#ffffff" opacity=".9">
            <rect x="12" y="80" width="22" height="22"/>
            <rect x="42" y="64" width="22" height="38"/>
            <rect x="72" y="46" width="22" height="56"/>
            <rect x="102" y="24" width="28" height="78"/>
          </g>
          <g fill="var(--red)" font-family="Roboto Condensed, sans-serif" font-size="9" font-weight="700">
            <text x="14" y="94">$100</text>
            <text x="44" y="78">$500</text>
            <text x="73" y="60">$1000</text>
            <text x="105" y="38">$2000</text>
          </g>
        </svg>
      </div>
      <div class="ways">
        <span>Through the school office</span>
        <span>By cheque to PVCS – PO Box 123 Parkridge NSW 2999</span>
        <span>Direct deposit A/C</span>
        <span class="site">pkrts.example.edu.au</span>
      </div>
    </div>
    <p class="notice">Number of partners and progress on money raised will be included in the Communicator each week during second term. Individual names will be kept confidential. Business names will be listed in the end of term Communicator and on the school web site.</p>
  </article>
</section>

</body>
</html>
```